Velmont Systems Business Card

Utilize the newly designed logo to create a polished, professional 2-sided business card for this IT Services company.

Target Market(s)

IT Professionals many in the telecommunications and medical industries.

Industry/Entity Type

Business

Requirements
Must have
• Use of new logo, identified color palette and font: Albertus MT Std Regular.

```html
<!DOCTYPE html>
<html lang="en">
<head>
<meta charset="utf-8">
<title>Velmont Systems Business Card</title>
<link href="https://fonts.googleapis.com/css2?family=Marcellus&family=Open+Sans:wght@400;600&display=swap" rel="stylesheet">
<style>
  :root {
    --navy: #1f3f94;
    --navy-deep: #0f4a97;
    --blue: #3b8bd0;
    --blue-mid: #2f7fcc;
    --cyan: #2fb3ea;
    --sky: #6fa0dc;
    --ink: #1c1c24;
    --text: #3a3a44;
    --paper: #f7fbfe;
    --backdrop: #ececec;
  }
  * { margin: 0; padding: 0; box-sizing: border-box; }
  html, body {
    width: 1200px; height: 1024px; overflow: hidden;
    background: var(--backdrop);
  }
  .canvas { position: relative; width: 1200px; height: 1024px; }

  .card {
    position: absolute; width: 700px; height: 400px; overflow: hidden;
    box-shadow: 0 4px 14px rgba(0,0,0,.18);
  }

  /* Front side */
  .card-front { left: 80px; top: 80px; background: var(--paper); }
  .card-front .edge-band {
    position: absolute; right: 0; top: 0; width: 46px; height: 100%;
    background: var(--navy-deep);
  }
  .brand {
    position: absolute; left: 48px; top: 56px;
    display: flex; align-items: center; gap: 18px;
  }
  .brand-dot {
    width: 70px; height: 70px; border-radius: 50%; background: var(--navy);
  }
  .brand-name {
    font-family: "Marcellus", serif; color: var(--navy);
    font-size: 40px; line-height: 1; letter-spacing: 1px; text-transform: uppercase;
  }
  .person { position: absolute; left: 48px; top: 168px; }
  .person-name {
    font-family: "Open Sans", sans-serif; font-size: 27px; color: var(--ink);
    letter-spacing: .5px;
  }
  .person-role {
    font-family: "Open Sans", sans-serif; font-size: 15px; color: var(--navy);
    margin-top: 2px;
  }
  .contacts {
    position: absolute; left: 48px; top: 246px; list-style: none;
    font-family: "Open Sans", sans-serif; font-size: 14px; color: var(--text);
  }
  .contacts li { display: flex; align-items: center; gap: 12px; height: 27px; }
  .contacts svg { width: 14px; height: 14px; fill: var(--navy); flex: none; }

  /* Back side */
  .card-back { left: 420px; top: 560px; background: var(--blue-mid); }
  .card-back .backdrop { position: absolute; inset: 0; }
  .back-brand {
    position: absolute; left: 0; right: 0; top: 148px;
    display: flex; align-items: center; justify-content: center; gap: 20px;
  }
  .back-brand .brand-dot { background: #ffffff; width: 64px; height: 64px; }
  .back-brand .brand-name { color: #ffffff; font-size: 46px; }
</style>
</head>
<body>
<main class="canvas">

  <section class="card card-front" aria-label="Business card front">
    <div class="edge-band"></div>
    <div class="brand">
      <span class="brand-dot"></span>
      <span class="brand-name">Velmont Systems</span>
    </div>
    <div class="person">
      <p class="person-name">Daniel Marsh</p>
      <p class="person-role">Manager</p>
    </div>
    <ul class="contacts">
      <li>
        <svg viewBox="0 0 14 14"><path d="M7 0a5 5 0 0 0-5 5c0 3.6 5 9 5 9s5-5.4 5-9a5 5 0 0 0-5-5zm0 7a2 2 0 1 1 0-4 2 2 0 0 1 0 4z"/></svg>
        PO Box 2784, Riverton BC, QLD, 4217
      </li>
      <li>
        <svg viewBox="0 0 14 14"><path d="M3 1l2.2 3-1.3 1.6a8 8 0 0 0 4.5 4.5L10 8.8l3 2.2-1.2 2.5C6.4 13.4.6 7.6.5 2.2z"/></svg>
        +61 400 512 968
      </li>
      <li>
        <svg viewBox="0 0 14 14"><path d="M0 3h14v8H0zm1 1v.3l6 3.9 6-3.9V4z" fill-rule="evenodd"/></svg>
        dmarsh@velmontsystems.com
      </li>
      <li>
        <svg viewBox="0 0 14 14"><circle cx="7" cy="7" r="6.5"/><path d="M.5 7h13M7 .5v13" stroke="#f7fbfe" stroke-width="1"/></svg>
        www.velmontsystems.com
      </li>
    </ul>
  </section>

  <section class="card card-back" aria-label="Business card back">
    <svg class="backdrop" viewBox="0 0 700 400" preserveAspectRatio="none">
      <rect width="700" height="400" fill="var(--blue-mid)"/>
      <path d="M0 0H560C400 30 250 90 150 200 90 270 50 330 0 400Z" fill="var(--navy)"/>
      <path d="M0 400C60 250 200 110 420 70 540 50 640 60 700 80V400Z" fill="var(--cyan)"/>
      <circle cx="470" cy="220" r="270" fill="var(--sky)" opacity=".55"/>
    </svg>
    <div class="back-brand">
      <span class="brand-dot"></span>
      <span class="brand-name">Velmont Systems</span>
    </div>
  </section>

</main>
</body>
</html>
```